Notes nobody handed you at college

Notes nobody handed you at college

"Unfiltered tips to help early career professionals successfully navigate the workplace"

I'VE INCLUDED LINKS TO SOME EXAMPLES OF COVERS THAT I LIKE.

Open to a creative concept. The book is sort of a guide for early career professionals and how they should navigate corporate America. Inside the book, I am giving tips on how to navigate work life. Most executive professionals have coaches, advisors and mentors to help them navigate the stressors of work. This is sort of a playbook for young professionals in the workplace.

Book Dimensions: 5.5" X 8.5"

Brightward Shift
https://www.plorvane.example/Brightward-Shift-Locating-Growing-Pleasing-ebook/dp/K47Q22TR8M/ref=sr_1_1?ie=UTF8&qid=1500000000&sr=8-1&keywords=brightward+shift

The Compass Ledger: Chart Your Calling. Outgrow Your Dread of Missteps. Apply Your Inborn Gifts And Abilities To Shape A Rewarding Path. https://www.plorvane.example/Compass-Ledger-Calling-Abilities-Rewarding-ebook/dp/K83W51LP0D/ref=pd_sim_351_11?_encoding=UTF8&psc=1&refRID=QTRA4KMWZBL2HDYC70XE

Cubicle Exit Route: Nine Moves to Launch a Kitchen-Table Venture, Leave the Office and Savor the Liberty: Features Talks with Warren Ode Hasket, Lyle Brantic, Gus Merrowby, Dale Finchum, Teodor Vasquill & more!
https://www.plorvane.example/Cubicle-Exit-Route-Talks-Vasquill-ebook/dp/K26H90YS44/ref=pd_sim_351_20?_encoding=UTF8&psc=1&refRID=LMPE3QDKWRZGB81VNTHA

The Quick Draft Calendar: The Lone Founder’s Handbook to Twelve Months of Article Topics in an Afternoon and Writing Pieces That Grip and Persuade
https://www.plorvane.example/Quick-Draft-Calendar-Founders-ebook/dp/K59F13BX7N/ref=pd_sim_351_4_encoding=UTF8&psc=1&refRID=GDUY46PKRJ0SMVCT2EQW

Crafting a Magnetic Landing Screen in Nine Easy Moves: Your Map to Storefront Landing Copy that Turns Browsers into Prospects & Buyers (Crafting Series... Volume 3)
https://www.plorvane.example/Crafting-Magnetic-Landing-Easy-Moves-ebook/dp/K38N67VC2J/ref=pd_sim_351_1?_encoding=UTF8&psc=1&refRID=RSOB45TQXFYMUHIKWDLE

Target Market(s)

College Students- Early Career Professionals

Industry/Entity Type

School

Font styles to use
Serif

Colors

Designer to choose colors to be used in the design.

Requirements
Must have
• Diversity in the cover- something eye catching. Photo on back cover. I'VE INCLUDED LINKS TO SOME EXAMPLES OF COVERS THAT I LIKE
Nice to have
• Designers have the flexibility to exert their creativity.I'VE INCLUDED LINKS TO SOME EXAMPLES OF COVERS THAT I LIKE
Should not have
• My picture on the cover

```html
<!DOCTYPE html>
<html lang="en">
<head>
<meta charset="utf-8">
<title>Notes Nobody Handed You at College – Book Cover</title>
<link href="https://fonts.googleapis.com/css2?family=Saira+Condensed:wght@500;600&family=Arimo:wght@400;700&display=swap" rel="stylesheet">
<style>
  :root {
    --stage: #f1f1f1;
    --cover: #c8ccd0;
    --cover-light: #d3d6d9;
    --ink: #2b2f38;
    --ink-soft: #33363c;
    --band: #2f343d;
    --spine: #c3c7cb;
    --photo-top: #bfb7b0;
    --photo-mid: #a7b4c8;
    --photo-low: #d6d9dc;
    --portrait-hair: #8a5a34;
    --portrait-suit: #2a2a2e;
  }
  * { box-sizing: border-box; margin: 0; padding: 0; }
  html, body {
    width: 1200px; height: 800px; overflow: hidden;
    background: var(--stage);
  }
  .jacket {
    position: absolute; left: 179px; top: 90px;
    width: 842px; height: 620px;
    display: flex;
    box-shadow: 0 10px 30px rgba(0,0,0,.18);
  }
  .back-cover {
    width: 401px; height: 620px; position: relative;
    background: var(--cover);
    font-family: "Arimo", Arial, sans-serif;
    color: var(--ink-soft);
  }
  .back-blurb {
    position: absolute; left: 26px; right: 26px; top: 42px;
    font-size: 11px; line-height: 1.42; text-align: justify;
  }
  .author-heading {
    position: absolute; left: 26px; top: 232px;
    font-size: 21px; font-weight: 700; color: var(--ink);
  }
  .author-bio {
    position: absolute; left: 26px; top: 264px; width: 176px;
    font-size: 11px; line-height: 1.42; text-align: justify;
  }
  .author-portrait {
    position: absolute; right: 22px; bottom: 0;
    width: 172px; height: 300px;
    background: linear-gradient(180deg, var(--cover) 0%, var(--portrait-hair) 22%, #6b4a36 40%, var(--portrait-suit) 62%, var(--portrait-suit) 100%);
    border-radius: 80px 80px 0 0;
  }
  .spine {
    width: 40px; height: 620px; position: relative;
    background: var(--spine);
    border-left: 1px solid rgba(0,0,0,.08);
    border-right: 1px solid rgba(0,0,0,.12);
  }
  .spine-title {
    position: absolute; left: 50%; top: 50%;
    transform: translate(-50%, -50%) rotate(90deg);
    white-space: nowrap;
    font-family: "Saira Condensed", "Arial Narrow", sans-serif;
    font-weight: 600; font-size: 17px; letter-spacing: 1px;
    color: var(--ink);
  }
  .front-cover {
    width: 401px; height: 620px; position: relative;
    background: var(--cover-light);
    overflow: hidden;
  }
  .cover-photo {
    position: absolute; left: 0; top: 0; width: 100%; height: 330px;
    background: linear-gradient(180deg, var(--photo-top) 0%, var(--photo-mid) 55%, var(--photo-low) 92%, var(--cover-light) 100%);
  }
  .cover-title {
    position: absolute; left: 0; right: 0; top: 326px;
    text-align: center;
    font-family: "Saira Condensed", "Arial Narrow", sans-serif;
    font-weight: 500; font-size: 52px; line-height: 1.02;
    letter-spacing: 1px; text-transform: uppercase;
    color: var(--ink);
  }
  .cover-subtitle {
    position: absolute; left: 30px; right: 30px; top: 522px;
    text-align: center;
    font-family: "Arimo", Arial, sans-serif;
    font-weight: 700; font-size: 12px; line-height: 1.35;
    color: var(--ink);
  }
  .cover-band {
    position: absolute; left: 0; right: 0; bottom: 0; height: 28px;
    background: var(--band);
  }
</style>
</head>
<body>
  <div class="jacket">
    <section class="back-cover">
      <p class="back-blurb">Lorem Ipsum is simply dummy text of the printing and typesetting industry. Lorem Ipsum has been the industry's standard dummy text ever since the 1500s, when an unknown printer took a galley of type and scrambled it to make a type specimen book. It has survived not only five centuries, but also the leap into electronic typesetting, remaining essentially unchanged. It was popularised in the 1960s with the release of Quillmark sheets containing Lorem Ipsum passages, and more recently with desktop publishing software like Vellory PageSmith including versions of Lorem Ipsum.</p>
      <h2 class="author-heading">Author</h2>
      <p class="author-bio">Lorem Ipsum is simply dummy text of the printing and typesetting industry. Lorem Ipsum has been the industry's standard dummy text ever since the 1500s, when an unknown printer took a galley of type and scrambled it to make a type specimen book. It has survived not only five centuries, but also the leap into electronic typesetting, remaining essentially unchanged. It was popularised in the 1960s with the release of Quillmark sheets containing Lorem Ipsum passages.</p>
      <div class="author-portrait" role="img" aria-label="Author portrait: smiling professional woman in a dark blazer, arms crossed"></div>
    </section>
    <div class="spine">
      <span class="spine-title">NOTES NOBODY HANDED YOU AT COLLEGE</span>
    </div>
    <section class="front-cover">
      <div class="cover-photo" role="img" aria-label="Photo of a stressed young office worker resting her head on her hand at a desk"></div>
      <h1 class="cover-title">Notes Nobody<br>Handed You<br>At College</h1>
      <p class="cover-subtitle">Unfiltered tips to help early career<br>professionals successfully navigate the workplace</p>
      <div class="cover-band"></div>
    </section>
  </div>
</body>
</html>
```